wealth management firm, professional group, new model

we have a logo that works but we need a card, white background using our colors...clean look

our tag line if can be used in

Guiding Every Client to Ownership

```html
<!DOCTYPE html>
<html lang="en">
<head>
<meta charset="utf-8">
<title>Calder Private Advisors – Business Card</title>
<link rel="stylesheet" href="https://fonts.googleapis.com/css2?family=Montserrat:wght@400;500&display=swap">
<style>
  :root {
    --backdrop: #262626;
    --card: #f1f1f1;
    --navy: #13264a;
  }
  * { box-sizing: border-box; margin: 0; padding: 0; }
  html, body {
    width: 1200px; height: 576px; overflow: hidden;
    background: var(--backdrop);
    font-family: "Montserrat", sans-serif;
    color: var(--navy);
  }
  .stage { position: relative; width: 1200px; height: 576px; }
  .card {
    position: absolute;
    width: 484px; height: 292px;
    background: var(--card);
    border-radius: 10px;
  }
  .card--front { left: 102px; top: 139px; }
  .card--back  { left: 596px; top: 138px; }

  .firm-name {
    position: absolute; text-align: center;
    font-weight: 500; letter-spacing: 0.01em; line-height: 1.15;
  }
  .firm-name__line { display: block; }

  .card--front .firm-name { left: 0; right: 0; top: 112px; }
  .card--front .firm-name__line { font-size: 34px; }

  .card--back .firm-name { left: 250px; width: 216px; top: 196px; }
  .card--back .firm-name__line { font-size: 24px; }
  .tagline {
    position: absolute; left: 250px; width: 216px; top: 262px;
    text-align: center; font-size: 9.5px; font-weight: 400; letter-spacing: 0.03em;
  }

  .person { position: absolute; left: 26px; top: 40px; }
  .person__name { font-size: 21px; font-weight: 500; line-height: 1.1; }
  .person__title { font-size: 13px; font-weight: 400; margin-top: 3px; }

  .contact { position: absolute; left: 26px; top: 208px; list-style: none; }
  .contact__item {
    display: flex; align-items: center; gap: 10px;
    font-size: 13px; height: 20.5px;
  }
  .contact__icon { width: 11px; height: 11px; fill: var(--navy); flex: none; }
</style>
</head>
<body>
<main class="stage">
  <section class="card card--front" aria-label="Card front">
    <div class="firm-name">
      <span class="firm-name__line">Calder</span>
      <span class="firm-name__line">Private Advisors</span>
    </div>
  </section>

  <section class="card card--back" aria-label="Card back">
    <div class="person">
      <h1 class="person__name">Daniel Reyes</h1>
      <p class="person__title">Managing Director</p>
    </div>

    <ul class="contact">
      <li class="contact__item">
        <svg class="contact__icon" viewBox="0 0 12 12" aria-hidden="true"><path d="M1 3.2C1 2 2.5 1 6 1s5 1 5 2.2V4.5H8.3V3.4H3.7v1.1H1z"/><path d="M3 5h6l1.6 5.5H1.4z"/></svg>
        <span>555-014-2278</span>
      </li>
      <li class="contact__item">
        <svg class="contact__icon" viewBox="0 0 12 12" aria-hidden="true"><path d="M0.5 2.5h11v7h-11z M1.5 3.3 6 6.8l4.5-3.5" fill="none" stroke="#13264a" stroke-width="1.4"/><path d="M0.5 2.5h11L6 6.6z"/></svg>
        <span>daniel@calderadvisors.com</span>
      </li>
      <li class="contact__item">
        <svg class="contact__icon" viewBox="0 0 12 12" aria-hidden="true"><g fill="none" stroke="#13264a" stroke-width="1.1"><circle cx="6" cy="6" r="5"/><ellipse cx="6" cy="6" rx="2.2" ry="5"/><path d="M1 6h10M2 3.3h8M2 8.7h8"/></g></svg>
        <span>www.calderadvisors.com</span>
      </li>
    </ul>

    <div class="firm-name">
      <span class="firm-name__line">Calder</span>
      <span class="firm-name__line">Private Advisors</span>
    </div>
    <p class="tagline">Guiding Every Client to Ownership</p>
  </section>
</main>
</body>
</html>
```